Mobile Crushing and Screening

Please design A5 double sided flyer, one side for Crusher other for screener. Please use photos, logo and wording in word document.
Main colours are Dark Green: #0B5D2A
Light Green: #8BC34A
please see our website www.brightridgeplant.com.au
Thank you

Requirements
Must have
• colour scheme as in website

```html
<!DOCTYPE html>
<html lang="en">
<head>
<meta charset="utf-8">
<title>Brightridge Plant – Mobile Crushing &amp; Screening Flyers</title>
<link href="https://fonts.googleapis.com/css2?family=Poppins:wght@400;500;600;700;800;900&display=swap" rel="stylesheet">
<style>
  :root {
    --dark-green: #0B5D2A;
    --light-green: #8BC34A;
    --lime: #c8d92a;
    --ink: #111512;
    --footer: #121614;
    --page: #5e5e60;
    --white: #ffffff;
  }
  * { box-sizing: border-box; margin: 0; padding: 0; }
  html, body { width: 1200px; height: 866px; overflow: hidden; }
  body {
    background: var(--page);
    font-family: "Poppins", sans-serif;
    position: relative;
  }
  .flyer {
    position: absolute;
    top: 111px;
    width: 460px;
    height: 646px;
    background: linear-gradient(to bottom, #fff 0 82%, #d9d9d9 90%);
    overflow: hidden;
  }
  .flyer--crushing { left: 118px; }
  .flyer--screening { left: 620px; }

  .hero {
    position: absolute; inset: 0 0 auto 0; height: 300px;
    background: radial-gradient(ellipse 60% 55% at 55% 78%, #e6e82a 0%, #5fb33a 30%, #1d7a35 58%, #0b3a1c 85%, #0a1a10 100%);
  }
  .flyer--screening .hero {
    background: radial-gradient(ellipse 60% 60% at 50% 55%, #6cc040 0%, #2a8a3a 35%, #0f5a28 65%, #0a1a10 100%);
  }
  .machine-photo {
    position: absolute;
    background: linear-gradient(160deg, #8a8a8a, #3a3a3a 55%, #1c1c1c);
    opacity: .85;
  }
  .flyer--crushing .machine-photo { left: 16px; top: 136px; width: 420px; height: 160px; border-radius: 6px 40px 4px 4px; }
  .flyer--screening .machine-photo { left: 40px; top: 120px; width: 400px; height: 176px; border-radius: 30px 30px 4px 4px; }
  .splash { position: absolute; left: 0; top: 230px; width: 460px; height: 90px; }

  .title {
    position: absolute; left: 30px; top: 26px;
    font-weight: 800; line-height: 1; color: var(--white);
  }
  .title__line { display: block; font-size: 37px; letter-spacing: .3px; }
  .title__line--accent { color: var(--lime); margin-top: 6px; }
  .title__sub { display: block; font-size: 16px; font-weight: 700; margin-top: 6px; }

  .brand {
    position: absolute; left: 279px; top: 28px;
    display: flex; align-items: center; gap: 8px;
  }
  .brand__ring { width: 28px; height: 28px; border-radius: 50%; background: var(--light-green); flex: none; }
  .brand__name { font-weight: 800; font-size: 15px; line-height: 1.05; color: var(--light-green); letter-spacing: .5px; }

  /* crushing content */
  .capability {
    position: absolute; left: 33px; top: 316px; width: 193px; height: 248px;
    border: 2px solid var(--dark-green); border-radius: 6px;
    padding: 0 12px; color: var(--dark-green);
  }
  .capability__title {
    position: absolute; top: -12px; left: 10px; background: #fff; padding: 0 4px;
    font-size: 21px; font-weight: 800; line-height: 1.2; width: 140px;
  }
  .capability__body { position: absolute; top: 60px; left: 14px; right: 8px; }
  .spec__label { font-weight: 700; font-size: 14px; color: var(--ink); }
  .spec__value { font-weight: 700; font-size: 17px; line-height: 1.15; }
  .spec__note { font-weight: 600; font-size: 10.5px; line-height: 1.2; }
  .spec + .spec { margin-top: 14px; }
  .capability__tip { margin-top: 12px; font-weight: 600; font-size: 10px; line-height: 1.3; }

  .we-heading { font-weight: 900; font-size: 33px; line-height: 1; color: var(--ink); white-space: nowrap; }
  .we-heading__we { color: var(--dark-green); }
  .flyer--crushing .we-heading { position: absolute; left: 245px; top: 306px; }

  .material-list { position: absolute; left: 248px; top: 349px; list-style: none; }
  .material-list li { display: flex; align-items: center; height: 34px; margin-bottom: 10px; }
  .swatch { width: 53px; height: 34px; flex: none; }
  .material-list .label { margin-left: 13px; font-weight: 700; font-size: 14.5px; color: var(--dark-green); line-height: 1.1; }
  .label small { display: block; font-weight: 400; font-size: 11px; color: var(--ink); line-height: 1.15; }

  .swatch--concrete { background: #9ea39c; }
  .swatch--brick { background: #a9482c; }
  .swatch--blocks { background: #b7b9b8; }
  .swatch--asphalt { background: #868b90; }
  .swatch--stone { background: #c99b5e; }
  .swatch--granite { background: #8e9090; }
  .swatch--soil { background: #8a5526; }
  .swatch--sand { background: #d9ad75; }
  .swatch--gravel { background: #7a7a7a; }

  /* screening content */
  .screen-box {
    position: absolute; left: 42px; top: 318px; width: 376px; height: 194px;
    border: 2px solid var(--dark-green); border-radius: 6px;
  }
  .screen-box .we-heading {
    position: absolute; top: -16px; left: 50%; transform: translateX(-50%);
    background: #fff; padding: 0 16px;
  }
  .screen-grid {
    position: absolute; left: 52px; top: 31px;
    display: grid; grid-template-columns: 164px 140px; row-gap: 15px; list-style: none;
  }
  .screen-grid li { display: flex; align-items: center; height: 34px; }
  .screen-grid .label { margin-left: 12px; font-weight: 700; font-size: 15px; color: var(--dark-green); }
  .screen-box__caption {
    position: absolute; bottom: -10px; left: 50%; transform: translateX(-50%);
    background: #fff; padding: 0 8px; white-space: nowrap;
    font-weight: 600; font-size: 12.5px; color: var(--dark-green);
  }
  .separation { position: absolute; left: 0; right: 0; top: 526px; text-align: center; }
  .separation__lead { font-weight: 600; font-size: 12px; color: var(--ink); }
  .separation__grades { font-weight: 800; font-size: 18.5px; color: var(--dark-green); line-height: 1.3; }

  .footer {
    position: absolute; left: 0; right: 0; bottom: 0; height: 67px;
    background: var(--footer);
    display: flex; align-items: center; padding-left: 30px;
  }
  .phone { display: flex; align-items: center; gap: 8px; font-weight: 700; font-size: 25px; color: var(--light-green); }
  .phone svg { width: 19px; height: 19px; }
  .contact { margin-left: 22px; font-size: 11px; color: #fff; line-height: 1.2; list-style: none; }
  .contact li { display: flex; align-items: center; gap: 8px; }
  .contact svg { width: 9px; height: 9px; }
</style>
</head>
<body>

<!-- Crushing side -->
<article class="flyer flyer--crushing">
  <div class="hero">
    <div class="machine-photo" role="img" aria-label="Tracked mobile jaw crusher with long discharge conveyor"></div>
    <svg class="splash" viewBox="0 0 460 90" preserveAspectRatio="none" aria-hidden="true">
      <path d="M0 70 C40 60 70 58 120 62 C200 60 260 50 330 38 C360 30 390 22 390 0 C400 30 380 50 370 55 L405 58 C420 60 450 62 460 68 L460 90 L0 90 Z" fill="#fff"/>
    </svg>
  </div>

  <h1 class="title">
    <span class="title__line">MOBILE</span>
    <span class="title__line title__line--accent">CRUSHING</span>
    <span class="title__sub">SERVICES</span>
  </h1>
  <div class="brand">
    <span class="brand__ring"></span>
    <span class="brand__name">BRIGHTRIDGE<br>PLANT</span>
  </div>

  <section class="capability">
    <h2 class="capability__title">TECHNICAL CAPABILITY</h2>
    <div class="capability__body">
      <div class="spec">
        <p class="spec__label">Production:</p>
        <p class="spec__value">5-50 tonnes / hr</p>
        <p class="spec__note">(dependent on feed<br>and output settings)</p>
      </div>
      <div class="spec">
        <p class="spec__label">Maximum Feed Size :</p>
        <p class="spec__value">Single Lump -<br>500 mm × 280 mm</p>
      </div>
      <p class="capability__tip">But for best performance<br>300mm material is preferred.</p>
    </div>
  </section>

  <h2 class="we-heading"><span class="we-heading__we">WE</span> CRUSH</h2>
  <ul class="material-list">
    <li><span class="swatch swatch--concrete" role="img" aria-label="Concrete rubble"></span><span class="label">CONCRETE</span></li>
    <li><span class="swatch swatch--brick" role="img" aria-label="Broken bricks"></span><span class="label">BRICK</span></li>
    <li><span class="swatch swatch--blocks" role="img" aria-label="Stone blocks"></span><span class="label">BLOCKS</span></li>
    <li><span class="swatch swatch--asphalt" role="img" aria-label="Asphalt surface"></span><span class="label">ASPHALT</span></li>
    <li><span class="swatch swatch--stone" role="img" aria-label="Natural sandstone"></span><span class="label">NATURAL STONE<small>(sandstone, limestone<br>and more)</small></span></li>
  </ul>

  <footer class="footer">
    <span class="phone">
      <svg viewBox="0 0 20 20" aria-hidden="true"><circle cx="10" cy="10" r="10" fill="#8BC34A"/><path d="M7 5l2 3-1.2 1.2a7 7 0 003 3L12 11l3 2-1 2c-4 0-9-5-9-9z" fill="#121614"/></svg>
      041 555 0192
    </span>
    <ul class="contact">
      <li><svg viewBox="0 0 10 10" aria-hidden="true"><path d="M1 1l8 3-3 1.5L8 9 6.8 9.6 5 6.2 3 8z" fill="#fff"/></svg>www.brightridgeplant.com.au</li>
      <li><svg viewBox="0 0 10 10" aria-hidden="true"><rect x="0" y="2" width="10" height="7" fill="#fff"/><path d="M0 2l5 4 5-4" stroke="#121614" fill="none"/></svg>info@brightridgeplant.com.au</li>
    </ul>
  </footer>
</article>

<!-- Screening side -->
<article class="flyer flyer--screening">
  <div class="hero">
    <div class="machine-photo" role="img" aria-label="Tracked mobile screener with side stockpile conveyors"></div>
    <svg class="splash" viewBox="0 0 460 90" preserveAspectRatio="none" aria-hidden="true">
      <path d="M0 80 C40 62 90 60 130 55 C200 60 260 62 310 50 C360 40 400 20 410 0 C420 20 400 35 395 40 L430 30 C410 50 420 60 460 72 L460 90 L0 90 Z" fill="#fff"/>
    </svg>
  </div>

  <h1 class="title">
    <span class="title__line">MOBILE</span>
    <span class="title__line title__line--accent">SCREENING</span>
    <span class="title__sub">SERVICES</span>
  </h1>
  <div class="brand">
    <span class="brand__ring"></span>
    <span class="brand__name">BRIGHTRIDGE<br>PLANT</span>
  </div>

  <section class="screen-box">
    <h2 class="we-heading"><span class="we-heading__we">WE</span> SCREEN</h2>
    <ul class="screen-grid">
      <li><span class="swatch swatch--concrete" role="img" aria-label="Concrete rubble"></span><span class="label">Concrete</span></li>
      <li><span class="swatch swatch--soil" role="img" aria-label="Soil"></span><span class="label">Soil</span></li>
      <li><span class="swatch swatch--brick" role="img" aria-label="Broken bricks"></span><span class="label">Brick</span></li>
      <li><span class="swatch swatch--sand" role="img" aria-label="Sand"></span><span class="label">Sand</span></li>
      <li><span class="swatch swatch--granite" role="img" aria-label="Stone"></span><span class="label">Stone</span></li>
      <li><span class="swatch swatch--gravel" role="img" aria-label="Gravel"></span><span class="label">Gravel</span></li>
    </ul>
    <p class="screen-box__caption">and other construction &amp; demolition materials</p>
  </section>

  <div class="separation">
    <p class="separation__lead">Accurate separation into</p>
    <p class="separation__grades">FINES • MEDIUM • OVERSIZED</p>
  </div>

  <footer class="footer">
    <span class="phone">
      <svg viewBox="0 0 20 20" aria-hidden="true"><circle cx="10" cy="10" r="10" fill="#8BC34A"/><path d="M7 5l2 3-1.2 1.2a7 7 0 003 3L12 11l3 2-1 2c-4 0-9-5-9-9z" fill="#121614"/></svg>
      041 555 0192
    </span>
    <ul class="contact">
      <li><svg viewBox="0 0 10 10" aria-hidden="true"><path d="M1 1l8 3-3 1.5L8 9 6.8 9.6 5 6.2 3 8z" fill="#fff"/></svg>www.brightridgeplant.com.au</li>
      <li><svg viewBox="0 0 10 10" aria-hidden="true"><rect x="0" y="2" width="10" height="7" fill="#fff"/><path d="M0 2l5 4 5-4" stroke="#121614" fill="none"/></svg>info@brightridgeplant.com.au</li>
    </ul>
  </footer>
</article>

</body>
</html>
```